Webdesign für Quellborn Lumen Kreis e.V.
Zielgruppe
Vereinsmitglieder aus der Bio-Tech-Branche, Öffentlichkeit
Aufgabenstellung
Wir benötigen ein Webdesign für die Website des Quellborn Lumen Kreis e.V., zu liefern als PSD-Datei.

```html
<!DOCTYPE html>
<html lang="de">
<head>
<meta charset="utf-8">
<title>Quellborn Lumen Kreis e.V.</title>
<link rel="stylesheet" href="https://fonts.googleapis.com/css2?family=Arimo:wght@400;700&display=swap">
<style>
  :root {
    --accent: #9ecbd8;
    --accent-line: #c9e0e8;
    --side-bg: #f6f4f5;
    --header-bg: #eef4f6;
    --text: #222222;
    --nav-text: #666666;
    --heading: #4f7d99;
    --rule: #aaaaaa;
    --white: #ffffff;
  }
  * { margin: 0; padding: 0; box-sizing: border-box; }
  html, body { width: 1185px; height: 1200px; overflow: hidden; }
  body { position: relative; background: var(--white); font-family: "Arimo", Arial, sans-serif; color: var(--text); }

  .site-header { position: absolute; left: 0; top: 0; width: 1185px; height: 187px;
    background: linear-gradient(180deg, #f3f7f8, var(--header-bg)); }
  .header-photo { position: absolute; left: 629px; top: 0; width: 556px; height: 187px;
    background: linear-gradient(90deg, #eef3f5 0%, #e2e9ee 35%, #d8dfe6 65%, #eceff2 100%); }
  .brand { position: absolute; left: 41px; top: 118px; display: flex; align-items: center; gap: 12px; }
  .brand-dot { width: 26px; height: 26px; border-radius: 50%; background: #3aa6b4; }
  .brand-name { font-size: 21px; letter-spacing: 3px; text-transform: uppercase; color: #1e2a30; font-weight: 400; }

  .accent-band { position: absolute; left: 1px; top: 191px; width: 1183px; height: 21px; background: var(--accent); }

  .sidebar-left { position: absolute; left: 0; top: 212px; width: 271px; height: 846px; background: var(--side-bg); }
  .main-nav { position: absolute; left: 0; top: 35px; width: 271px; list-style: none; }
  .main-nav li { height: 49px; border-bottom: 2px solid var(--accent-line); font-size: 22px;
    font-variant: small-caps; color: var(--nav-text); padding: 12px 0 0 42px; }
  .main-nav li.is-active { background: var(--accent); color: var(--white); border-bottom-color: var(--accent); }
  .search { position: absolute; left: 42px; top: 700px; }
  .search-label { font-size: 20px; font-variant: small-caps; color: var(--nav-text); display: block; margin-bottom: 6px; }
  .search-input { width: 187px; height: 39px; border: 1px solid #cfcfcf; background: var(--white); }

  .content { position: absolute; left: 272px; top: 212px; width: 638px; height: 846px; background: var(--white); }
  .hero { position: absolute; left: 39px; top: 41px; width: 563px; height: 308px;
    background: linear-gradient(135deg, #dfe6ea 0%, #c9d3da 40%, #e6ebee 100%); }
  .hero-caption { position: absolute; left: 0; bottom: 0; width: 100%; height: 110px;
    background: rgba(170, 210, 222, 0.85); color: var(--white); font-size: 27px; padding: 50px 0 0 23px; }
  .intro-title { position: absolute; left: 39px; top: 383px; font-size: 26px; font-weight: 400; color: var(--heading); }
  .intro-image { position: absolute; left: 40px; top: 435px; width: 132px; height: 170px; border: 1px solid #d5d5d5;
    background: linear-gradient(160deg, #eef1f3, #d6dee4 60%, #c8d8e6); }
  .intro-text { position: absolute; left: 199px; top: 434px; width: 400px; font-size: 17px; line-height: 21.3px; }
  .content-rule { position: absolute; left: 36px; top: 690px; width: 534px; height: 2px; background: var(--rule); }

  .sidebar-right { position: absolute; left: 910px; top: 212px; width: 275px; height: 846px; background: var(--side-bg); }
  .languages { position: absolute; left: 115px; top: 22px; display: flex; gap: 10px; }
  .languages svg { width: 33px; height: 21px; display: block; }
  .event { position: absolute; left: 20px; width: 212px; }
  .event-title { height: 34px; background: var(--accent); color: var(--white); font-size: 20px; font-weight: 400;
    text-transform: uppercase; padding: 5px 0 0 18px; }
  .event-info { font-size: 17px; line-height: 21px; padding: 15px 0 0 18px; }
  .event-info p + p { margin-top: 21px; }
  .side-decoration { position: absolute; left: 107px; top: 620px; width: 168px; height: 226px;
    background: radial-gradient(ellipse at 60% 50%, #d4e4ee 0%, rgba(246,244,245,0) 70%); }

  .site-footer { position: absolute; left: 0; top: 1058px; width: 1185px; height: 142px;
    border-top: 2px solid #e6e6e6; background: linear-gradient(180deg, #ffffff 0%, #d6e8ec 100%);
    text-align: center; font-size: 18.5px; color: #333333; padding-top: 67px; }
</style>
</head>
<body>
  <header class="site-header">
    <div class="brand">
      <span class="brand-dot"></span>
      <span class="brand-name">Quellborn Lumen Kreis</span>
    </div>
    <div class="header-photo" role="img" aria-label="Foto: Forscherin im Labor mit DNA-Modell"></div>
  </header>
  <div class="accent-band"></div>

  <aside class="sidebar-left">
    <ul class="main-nav">
      <li>Über uns</li>
      <li>Veranstaltungen</li>
      <li>Aktuelles</li>
      <li>Region</li>
      <li class="is-active">Service</li>
      <li>Kontakt</li>
    </ul>
    <div class="search">
      <span class="search-label">Suchen</span>
      <div class="search-input"></div>
    </div>
  </aside>

  <main class="content">
    <div class="hero" role="img" aria-label="Foto: zwei Forschende im Labor">
      <div class="hero-caption">New improved technologies</div>
    </div>
    <h1 class="intro-title">Quellborn Lumen Kreis</h1>
    <div class="intro-image" role="img" aria-label="Foto: Forscherin mit DNA-Modell"></div>
    <p class="intro-text">
      Der Quellborn Lumen Kreis ist ein<br>
      Zusammen-schluß von Wissenschaftlern,<br>
      Unternehmern und Dienst-leistern, die<br>
      die biotechno-logische Forschung in der Region<br>
      Frankfurt /Rhein-Main voranbringen wollen.<br>
      Wir sind qualifizierter Ansprech-partner wenn<br>
      es darum geht, Forschungsideen zu bewerten,<br>
      umzusetzen und zu kommunizieren.<br>
      Dazu bieten wir Plattformen und Arbeitskreise an<br>
      und führen selbst Studien durch.
    </p>
    <div class="content-rule"></div>
  </main>

  <aside class="sidebar-right">
    <div class="languages">
      <svg viewBox="0 0 33 21" aria-label="Deutsch"><rect width="33" height="7" fill="#000"/><rect y="7" width="33" height="7" fill="#dd0000"/><rect y="14" width="33" height="7" fill="#ffce00"/></svg>
      <svg viewBox="0 0 33 21" aria-label="English"><rect width="33" height="21" fill="#012169"/><path d="M0 0L33 21M33 0L0 21" stroke="#fff" stroke-width="4"/><path d="M0 0L33 21M33 0L0 21" stroke="#c8102e" stroke-width="1.5"/><path d="M16.5 0V21M0 10.5H33" stroke="#fff" stroke-width="6"/><path d="M16.5 0V21M0 10.5H33" stroke="#c8102e" stroke-width="3.5"/></svg>
      <svg viewBox="0 0 33 21" aria-label="Français"><rect width="11" height="21" fill="#0055a4"/><rect x="11" width="11" height="21" fill="#fff"/><rect x="22" width="11" height="21" fill="#ef4135"/></svg>
    </div>
    <section class="event" style="top: 67px;">
      <h2 class="event-title">Veranstaltung</h2>
      <div class="event-info">
        <p>Veranstaltung 1<br>12345 Quellborn<br>Lumenstr.&nbsp; 1</p>
        <p>13.November 2010<br>14:00 Uhr</p>
      </div>
    </section>
    <section class="event" style="top: 311px;">
      <h2 class="event-title">Veranstaltung</h2>
      <div class="event-info">
        <p>Veranstaltung 1<br>12345 Quellborn<br>Lumenstr.&nbsp; 1</p>
        <p>13.November 2010<br>14:00 Uhr</p>
      </div>
    </section>
    <div class="side-decoration" role="img" aria-label="Dekorative DNA-Doppelhelix"></div>
  </aside>

  <footer class="site-footer">(c) 2010 | Quellborn Lumen Kreis e.V. | Kontakt | Impressum</footer>
</body>
</html>
```